Postcard designed to acquire new customers

Need a postcard style AD to place in dentist offices and other professionals to promote our tax saving system. We will place these in dentists offices, orthodontist, optometrist, physiotherapist and all sorts of medical/dental offices. The card should highlight how they can save taxes by using our software. Our website has good information on it, and I'll include the advertising PDF that our software company produces. Our logo is a little out-dated and I've included the bonus of the winner re-making the logo so its better than it currently is.
Updates

I don't need to have any space allocated for a stamp and address. We are using this to place in offices and are for advertising purposes, not mailing. Thanks!

Reason: My apologies for not providing feedback yet, I've lost several days due to some illness and am finally back at work. I'll be going through designs today and would like the extra few days to work with many of you to create a great design. Thank you for your patience! Doyle

Reason: Again, my apologies for the delay. I will be in contact with designers this week. Thank you,

Target Market(s)

Small Business Owners in Canada

Industry/Entity Type

Health Insurance

Logo Text

Save Time, Save Money

Font styles to use
Other font styles liked:
• Easy to Read Font's

Colors

Designer to choose colors to be used in the design.

Requirements
Must have
• Must have a call to action on the postcard to sell the service. We need people to have their attention caught. A call to action could be, "You're spending too much on taxes! That's what they'll say if your business doesn't have a 789 Brookvale Outlay Plan..."
• See the PDF for other catch phrases or key information on what a Health Spending Account is. Many people don't know so I'd like to see 3-4 bullet points on the front of the postcard on what a health spending account is. See the attached PDF for that information and simplifying the information to short bullet points would be best. Here are my thoughts:
• Who should have a 789 Brookvale Outlay Plan?
• - Every business owner who is incorporated should have one.
• - Write off 100% of this QTB approved this method.
• - It is the most tax effective way to run dental, health, vision and other expenses through your company.
• - Easy to use APP for your phone, 2-day turnaround time for claims
• If you aren't using this, you're throwing tax dollars away!
• The back of the postcard would include 2 things. First, an example of the taxes you can save, and second - the different information they can send us so we can setup your account.
• First is the example of how this saves you money. Assuming a 38% personal tax rate. You will need to earn $1.62 of gross income, pay $0.62 of personal tax, which leaves you with $1.00 of after tax money to use for your personal expenses.
• The example of using a 789 Brookvale Outlay Plan, or doing nothing would need the following information.
• Comparison
• $5,000 of medical, dental, vision expenses
• Do Nothing 789 Brookvale Outlay Plan
• $8,100 – Total Cost $5,525 – Total Cost
• $3,100 – Income Tax $500 fee & $25 GST
• $5,000 – Money needed for medical, dental, vision, etc. $5,000 – Money needed for medical, dental, vision, etc.
• SAVINGS is $2,575
• Assuming a company incorporated in Alberta and a one time setup fee of $275 has not been included in the comparison.
• Information to send us to setup your account is:
• - Names and birth dates of you and your dependents
• - Contact information for you and your business (if different) Address, email, phone numbers
• - We will contact you about how to setup the app, your banking details and some other items.
• - Setup fee is a one-time payment of $275
Nice to have
• I'd like the front of the postcard to not be very busy with the background or graphics, etc. I want the call to action to be very obvious so they want to read the bullet points and look at the back of the postcard for more information.

```html
<!DOCTYPE html>
<html lang="en">
<head>
<meta charset="utf-8">
<title>789 Brookvale Outlay Plan – Postcard</title>
<link href="https://fonts.googleapis.com/css2?family=Open+Sans:wght@400;600;700;800&display=swap" rel="stylesheet">
<style>
:root{
  --orange:#f39a1e;
  --orange-deep:#e07b12;
  --charcoal:#2b2b2d;
  --charcoal-2:#3c3c3f;
  --ink:#2a2a2a;
  --muted:#6d6d6d;
  --paper:#ffffff;
  --line:#d9d9d9;
  --photo-a:#8e9399;
  --photo-b:#c8ccd1;
}
*{box-sizing:border-box;margin:0;padding:0}
html,body{width:891px;height:1200px;overflow:hidden;background:#fff;font-family:"Open Sans",Arial,sans-serif;color:var(--ink)}
.canvas{position:relative;width:891px;height:1200px}
.side-label{position:absolute;left:845px;width:46px;display:flex;align-items:center;justify-content:center;font-size:13px;font-weight:700;letter-spacing:2px;color:#555;writing-mode:vertical-rl}
.side-label.front{top:10px;height:570px}
.side-label.back{top:600px;height:590px}

/* FRONT */
.card{position:absolute;left:8px;width:835px;overflow:hidden;background:var(--paper);box-shadow:0 0 0 1px #e4e4e4}
.card.front{top:8px;height:572px}
.front .top-band{position:absolute;left:0;top:0;width:835px;height:250px;background:linear-gradient(180deg,#444447,var(--charcoal))}
.front .stripes{position:absolute;left:0;top:0}
.front .photo{position:absolute;right:0;top:0;width:420px;height:345px;background:linear-gradient(160deg,var(--photo-b),var(--photo-a))}
.brand{position:absolute;left:14px;top:8px;display:flex;align-items:center;gap:8px;background:#fff;padding:6px 10px;border-radius:3px}
.brand .mark{width:22px;height:22px;background:var(--orange)}
.brand .name{font-size:12px;font-weight:800;color:var(--charcoal);line-height:1.1;text-transform:uppercase}
.brand .tag{font-size:7px;font-weight:600;color:var(--muted);letter-spacing:.5px}
.headline{position:absolute;left:24px;top:58px;width:380px;padding:16px 18px;background:rgba(30,30,32,.92);border:2px solid var(--orange);border-radius:6px;color:#fff;text-align:center;font-size:20px;font-weight:700;line-height:1.3}
.headline .plan{color:var(--orange);font-weight:800;text-transform:uppercase;font-size:21px}
.who{position:absolute;left:18px;top:262px;white-space:nowrap;background:#fff;border-left:6px solid var(--orange);padding:6px 12px;font-size:15px;font-weight:800;color:var(--charcoal);box-shadow:0 2px 4px rgba(0,0,0,.15)}
.bullets{position:absolute;left:22px;top:310px;width:385px;list-style:none}
.bullets li{display:flex;gap:10px;align-items:flex-start;font-size:13.5px;font-weight:600;line-height:1.3;margin-bottom:8px;color:var(--ink)}
.bullets svg{flex:none;margin-top:1px}
.contact{position:absolute;right:14px;top:330px;width:235px;text-align:center}
.contact .speak{display:block;background:var(--charcoal);color:#fff;font-size:12px;font-weight:700;padding:5px 0;letter-spacing:.5px}
.contact .phone{display:block;background:#fff;border:2px solid var(--charcoal);font-size:30px;font-weight:800;color:var(--charcoal);padding:4px 0}
.contact .visit{display:inline-block;margin-top:10px;background:var(--orange);color:#fff;font-size:12px;font-weight:700;padding:4px 14px}
.front .bottom-band{position:absolute;left:0;bottom:0}
.website{position:absolute;right:20px;bottom:34px;color:#fff;font-size:17px;font-weight:700;display:flex;align-items:center;gap:6px}

/* BACK */
.card.back{top:600px;height:592px}
.back .col{position:absolute;left:18px;top:18px;width:470px}
.section-head{border-left:6px solid var(--orange);padding:4px 10px;font-size:15px;font-weight:800;text-transform:uppercase;color:var(--charcoal);background:#f3f3f3;margin-bottom:10px}
.back p{font-size:12px;line-height:1.4;margin-bottom:8px}
.back .orange{color:var(--orange-deep);font-weight:700}
.compare{list-style:none;font-size:12px;line-height:1.45;margin-bottom:14px}
.compare li{display:flex;gap:6px}
.compare li::before{content:"";flex:none;width:7px;height:7px;margin-top:6px;background:var(--orange)}
.compare .amt{color:var(--orange-deep);font-weight:700}
.setup{list-style:none;font-size:12px;line-height:1.4}
.setup li{display:flex;gap:6px;margin-bottom:4px}
.setup li::before{content:"";flex:none;width:7px;height:7px;margin-top:5px;background:var(--orange)}
.back .skyline{position:absolute;right:0;top:250px;width:345px;height:110px;background:linear-gradient(180deg,#ffffff,#e5e7ea)}
.postage{position:absolute;right:18px;top:60px;width:150px;height:110px;border:1px solid var(--line);display:flex;align-items:center;justify-content:center;font-size:13px;color:var(--muted)}
.address-area{position:absolute;right:80px;top:380px;font-size:13px;color:var(--muted)}
.barcode-area{position:absolute;right:80px;top:508px;font-size:13px;color:var(--muted)}
.back .divider{position:absolute;left:500px;top:40px;width:1px;height:520px;background:var(--line)}
.back .bar{position:absolute;left:0;bottom:0;width:835px;height:8px;background:var(--orange)}
</style>
</head>
<body>
<div class="canvas">

  <section class="card front">
    <div class="top-band"></div>
    <div class="photo" role="img" aria-label="Business people walking in a bright city office lobby"></div>
    <svg class="stripes" width="835" height="250" viewBox="0 0 835 250">
      <polygon points="300,0 380,0 250,250 170,250" fill="#f39a1e" opacity=".85"/>
      <polygon points="390,0 415,0 285,250 260,250" fill="#f39a1e" opacity=".6"/>
    </svg>

    <div class="brand">
      <span class="mark"></span>
      <div>
        <div class="name">789 Brookvale<br>Outlay Plan</div>
        <div class="tag">SAVE TIME, SAVE MONEY</div>
      </div>
    </div>

    <div class="headline">
      You're spending too much on taxes! That's what they'll say if your business doesn't have a
      <span class="plan">789 Brookvale Outlay Plan...</span>
    </div>

    <div class="who">Who should have a 789 Brookvale Outlay Plan?</div>

    <ul class="bullets">
      <li><svg width="18" height="18" viewBox="0 0 18 18"><circle cx="9" cy="9" r="9" fill="#f39a1e"/><path d="M5 9.5l2.6 2.6L13 6.5" stroke="#fff" stroke-width="2" fill="none"/></svg>Every business owner who is incorporated should have one.</li>
      <li><svg width="18" height="18" viewBox="0 0 18 18"><circle cx="9" cy="9" r="9" fill="#f39a1e"/><path d="M5 9.5l2.6 2.6L13 6.5" stroke="#fff" stroke-width="2" fill="none"/></svg>Write off 100% of this QTB approved this method.</li>
      <li><svg width="18" height="18" viewBox="0 0 18 18"><circle cx="9" cy="9" r="9" fill="#f39a1e"/><path d="M5 9.5l2.6 2.6L13 6.5" stroke="#fff" stroke-width="2" fill="none"/></svg>It is the most tax effective way to run dental, health, vision and other expenses through your company.</li>
      <li><svg width="18" height="18" viewBox="0 0 18 18"><circle cx="9" cy="9" r="9" fill="#f39a1e"/><path d="M5 9.5l2.6 2.6L13 6.5" stroke="#fff" stroke-width="2" fill="none"/></svg>Easy to use APP for your phone, 2-day turnaround time for claims</li>
      <li><svg width="18" height="18" viewBox="0 0 18 18"><circle cx="9" cy="9" r="9" fill="#f39a1e"/><path d="M5 9.5l2.6 2.6L13 6.5" stroke="#fff" stroke-width="2" fill="none"/></svg>If you aren't using this, you're throwing tax dollars away!</li>
    </ul>

    <div class="contact">
      <span class="speak">SPEAK WITH OUR EXPERT:</span>
      <span class="phone">0190 555 274</span>
      <span class="visit">Visit our Website</span>
    </div>

    <svg class="bottom-band" width="835" height="90" viewBox="0 0 835 90">
      <path d="M0,40 Q420,0 835,30 L835,90 L0,90 Z" fill="#f39a1e"/>
      <path d="M0,52 Q420,12 835,40 L835,90 L0,90 Z" fill="#2b2b2d"/>
    </svg>
    <div class="website">
      <svg width="16" height="16" viewBox="0 0 16 16"><circle cx="8" cy="8" r="7" fill="none" stroke="#f39a1e" stroke-width="1.6"/><path d="M1 8h14M8 1c3 3 3 11 0 14M8 1c-3 3-3 11 0 14" stroke="#f39a1e" stroke-width="1.2" fill="none"/></svg>
      www.brookvaleoutlay.com
    </div>
  </section>
  <div class="side-label front">FRONT</div>

  <section class="card back">
    <div class="col">
      <h2 class="section-head">An example of the taxes you can save</h2>
      <p>First is the example of how this saves you money. Assuming a 38% personal tax rate. You will need to earn $1.62 of gross income, pay $0.62 of personal tax, which leaves you with $1.00 of after tax money to use for your personal expenses.</p>
      <p class="orange">The example of using a 789 Brookvale Outlay Plan, or doing nothing would need the following information.</p>
      <ul class="compare">
        <li>Comparison</li>
        <li><span><span class="amt">$5,000</span> of medical, dental, vision expenses</span></li>
        <li>Do Nothing &nbsp; 789 Brookvale Outlay Plan</li>
        <li><span><span class="amt">$8,100</span> – Total Cost &nbsp; <span class="amt">$5,525</span> – Total Cost</span></li>
        <li><span><span class="amt">$3,100</span> – Income Tax &nbsp; <span class="amt">$500</span> fee &amp; <span class="amt">$25</span> GST</span></li>
        <li><span><span class="amt">$5,000</span> – Money needed for medical, dental, vision, etc. &nbsp; <span class="amt">$5,000</span> – Money needed for medical, dental, vision, etc.</span></li>
        <li><span>SAVINGS is <span class="amt">$2,575</span></span></li>
        <li><span>Assuming a company incorporated in Alberta and a one time setup fee of <span class="amt">$275</span> has not been included in the comparison.</span></li>
      </ul>

      <h2 class="section-head">Information to send us to setup your account is</h2>
      <ul class="setup">
        <li>Names and birth dates of you and your dependents</li>
        <li>Contact information for you and your business (if different) Address, email, phone numbers</li>
        <li>We will contact you about how to setup the app, your banking details and some other items.</li>
        <li>Setup fee is a one-time payment of $275</li>
      </ul>
    </div>

    <div class="divider"></div>
    <div class="skyline" role="img" aria-label="Faint city skyline silhouette"></div>
    <div class="postage">Postage Area</div>
    <div class="address-area">Address Area</div>
    <div class="barcode-area">Barcode Area</div>
    <div class="bar"></div>
  </section>
  <div class="side-label back">BACK</div>

</div>
</body>
</html>
```